Cloud Software Services Business Card Design Challenge

We are seeking a fresh and creative business card design that aligns with the brand identity of a startup cloud software services company. As a company specializing in advanced cloud solutions, we want these business cards to reflect our technological leadership and professionalism, helping us stand out in business communications and emphasize our core values.

About Us: We are dedicated to supporting the digital transformation of interior design companies through efficient, reliable, and innovative cloud software services. Our goal is to provide the best technological solutions to drive continuous growth and success for our clients.

Design Requirements:

• Colors: We have not yet established a final color scheme, so please do not feel constrained by the current logo colors. The logo colors can be adjusted according to the overall design. We would like you to choose colors based on your design concept, considering a minimalist, professional, and high-end palette. While many tech companies use a lot of blue, we prefer to avoid this common approach, so feel free to explore other color options.

• Style: The business card design should be modern, clean, and professional, reflecting our technological leadership and innovation capabilities. The design should have a strong visual impact and showcase our expertise in cloud technology.

• Visual Elements: We want the overall feel to be simple and clean. Consider incorporating technology-inspired design elements, such as sleek lines or geometric shapes, to enhance our brand's modern tech image.

• Final Design: The business card should have clear readability and a logical layout, and be suitable for various physical media. The design should accurately reflect our company's professional image and innovative capabilities in the cloud software services field.

• Information Layout: The card should include the following details (we will provide the details for 1 name after selecting the winner and ask the designer to provide four final information of the same design—
1. Chinese version with the job title
2. Chinese version without the job title
3. English version with the job title
4. English version without the job title
o Name
o Job Title
o Company Name and Address
o Tax ID Number
o Phone Number
o Email Address
o Company Website URL
o QR Code

We look forward to seeing how your design can showcase our excellence and professionalism in the cloud software services industry. We hope your creativity will help us effectively communicate our brand values!

Target Market(s)

Interior Design Companies

Contact Information for Business Card

The card should include the following details (we will provide the details for 1 name after selecting the winner and ask the designer to provide four final information of the same design— 1. Chinese version with the job title 2. Chinese version without the job title 3. English version with the job title 4. English version without the job title o Name o Job Title o Company Name and Address o Tax ID Number o Phone Number o Email Address o Company Website URL o QR Code

Colors
0054AA
0677BA
7BADD7
CADEEF
E8F1F8
0094D4
00A9DD
6FCCEA
C7EBF8
E9F6FB
00AB8E
00BBA5
67D7C9
C6EFE9
E9F9F6
FFC000
F8CF3A
FAE287
FDF2CF
FEFAEE
F0912C
F2A743
F7CA91
FBE8D2
FDF5EE
EE7325
F08F49
F5BC92
FAE3D3
FDF4ED
A7469A
B969AE
D3A5CF
EDDBEB
F8F0F9
6B429C
8869AF
B7A5CE
E3DAEB
F3F0F8

```html
<!DOCTYPE html>
<html lang="en">
<head>
<meta charset="utf-8">
<title>Veloxa Business Card</title>
<link rel="stylesheet" href="https://fonts.googleapis.com/css2?family=Outfit:wght@300;400;600;700&display=swap">
<style>
  :root {
    --stage: #454545;
    --ink: #0b0b0b;
    --paper: #ffffff;
    --text-light: #f4f4f4;
    --icon: #c9c9c9;
    --silver-1: #a4a4a4;
    --silver-2: #e9e9e9;
    --silver-3: #bcbcbc;
    --silver-4: #f5f5f5;
    --silver-5: #9a9a9a;
  }
  * { box-sizing: border-box; margin: 0; padding: 0; }
  html, body {
    width: 1200px; height: 1200px; overflow: hidden;
    background: var(--stage);
    font-family: "Outfit", sans-serif;
  }
  .canvas { position: relative; width: 1200px; height: 1200px; }
  .card {
    position: absolute; left: 166px; width: 866px; height: 506px;
    overflow: hidden; background: var(--ink);
    box-shadow: 0 2px 6px rgba(0,0,0,0.35);
  }
  .card--front { top: 79px; }
  .card--back { top: 647px; background: var(--paper); }
  .card__art { position: absolute; inset: 0; width: 100%; height: 100%; display: block; }

  .brand {
    position: absolute; display: flex; align-items: center; gap: 14px;
    font-weight: 700; letter-spacing: 0.08em; line-height: 1;
  }
  .brand__dot { border-radius: 50%; flex: none; }
  .brand--front { left: 62px; top: 232px; color: var(--ink); font-size: 46px; }
  .brand--front .brand__dot { width: 26px; height: 26px; background: var(--ink); }
  .brand--back { left: 390px; top: 146px; color: var(--paper); font-size: 42px; }
  .brand--back .brand__dot { width: 20px; height: 20px; background: var(--paper); }

  .identity { position: absolute; right: 64px; top: 95px; text-align: right; color: var(--text-light); }
  .identity__name { font-weight: 600; font-size: 33px; line-height: 40px; }
  .identity__role { font-weight: 300; font-size: 23px; line-height: 34px; margin-top: 4px; }

  .contact { position: absolute; right: 38px; top: 333px; list-style: none; color: var(--text-light); }
  .contact__item {
    display: flex; justify-content: flex-end; align-items: center; gap: 16px;
    font-weight: 300; font-size: 23px; line-height: 39px;
  }
  .contact__icon { width: 16px; height: 16px; fill: var(--icon); flex: none; }
</style>
</head>
<body>
<main class="canvas">

  <section class="card card--front" aria-label="Business card front">
    <svg class="card__art" viewBox="0 0 693 405" preserveAspectRatio="none" aria-hidden="true">
      <defs>
        <linearGradient id="silver-front" x1="0" y1="0" x2="1" y2="1">
          <stop offset="0" stop-color="var(--silver-1)"/>
          <stop offset="0.3" stop-color="var(--silver-2)"/>
          <stop offset="0.55" stop-color="var(--silver-3)"/>
          <stop offset="0.75" stop-color="var(--silver-4)"/>
          <stop offset="1" stop-color="var(--silver-5)"/>
        </linearGradient>
      </defs>
      <polygon class="panel-white" fill="var(--paper)" points="0,0 219,0 315,175 190,405 0,405"/>
      <polygon class="chevron-stripe" fill="url(#silver-front)" points="283,37 327,37 391,152 257,405 215,405 345,152"/>
      <polygon class="slash-stripe" fill="url(#silver-front)" points="384,203 407,203 307,405 282,405"/>
    </svg>

    <div class="brand brand--front"><span class="brand__dot"></span>VELOXA</div>

    <div class="identity">
      <p class="identity__name">Your Name</p>
      <p class="identity__role">Designation</p>
    </div>

    <ul class="contact">
      <li class="contact__item">1234 567890
        <svg class="contact__icon" viewBox="0 0 16 16" aria-hidden="true"><path d="M4 1.5 6 4.8 4.7 6.4c.8 1.9 2.5 3.7 4.9 4.9l1.6-1.3 3.3 2-1 2.4C8 14.6 1.4 8 1.6 2.5z"/></svg>
      </li>
      <li class="contact__item">info@veloxa.com.au
        <svg class="contact__icon" viewBox="0 0 16 16" aria-hidden="true"><path d="M1 3h14v10H1z M2 4.2v.6l6 4 6-4v-.6z" fill-rule="evenodd"/></svg>
      </li>
      <li class="contact__item">veloxa.com.au
        <svg class="contact__icon" viewBox="0 0 16 16" aria-hidden="true"><path d="M8 1a7 7 0 1 0 0 14A7 7 0 0 0 8 1zm0 1.4c.9 0 1.8 1.9 2 4.6H6c.2-2.7 1.1-4.6 2-4.6zM2.5 7.3h2.3c0-1.6.3-3 .8-4A5.7 5.7 0 0 0 2.5 7.3zm0 1.4a5.7 5.7 0 0 0 3.1 4c-.5-1-.8-2.4-.8-4zm3.5 0h4c-.2 2.7-1.1 4.6-2 4.6s-1.8-1.9-2-4.6zm5.2 0c0 1.6-.3 3-.8 4a5.7 5.7 0 0 0 3.1-4zm0-1.4h2.3a5.7 5.7 0 0 0-3.1-4c.5 1 .8 2.4.8 4z"/></svg>
      </li>
    </ul>
  </section>

  <section class="card card--back" aria-label="Business card back">
    <svg class="card__art" viewBox="0 0 693 404" preserveAspectRatio="none" aria-hidden="true">
      <defs>
        <linearGradient id="silver-back" x1="0" y1="0" x2="1" y2="0.4">
          <stop offset="0" stop-color="var(--silver-1)"/>
          <stop offset="0.25" stop-color="var(--silver-4)"/>
          <stop offset="0.45" stop-color="var(--silver-3)"/>
          <stop offset="0.65" stop-color="var(--silver-2)"/>
          <stop offset="0.85" stop-color="var(--silver-4)"/>
          <stop offset="1" stop-color="var(--silver-1)"/>
        </linearGradient>
      </defs>
      <polygon class="panel-black" fill="var(--ink)" points="0,0 693,0 693,170 484,297 0,44"/>
      <polygon class="chevron-band" fill="url(#silver-back)" points="0,44 484,297 693,170 693,252 484,375 0,119"/>
      <polygon class="lower-stripe" fill="url(#silver-back)" points="0,170 382,367 382,404 362,404 0,217"/>
      <polygon class="corner-black" fill="var(--ink)" points="0,217 362,404 0,404"/>
    </svg>

    <div class="brand brand--back"><span class="brand__dot"></span>VELOXA</div>
  </section>

</main>
</body>
</html>
```